Harlow Stonefield Civil Construction website design

We want a Bold website to promote our Heavy Civil Construction company, We would like an organic / tangible feel to the site. The pictures will be over saturated so they pop. We need to be able to easliy upload new projects and pictures on a regular basis.
Home page will have a full screen width image, "home page image" with silhouette and logo. It will also have about us area and picture
Page 2 will be Project Gallery with pictures in project folders
Page 3 will be an employment application form and submission
Page 4 will be Contact Us
Target Market(s)
Construction indusrty
Industry/Entity Type
Contractor
Coding
Coded - Design and coding required
Number of Pages Required
4 page
Font styles to use
Other font styles liked:
- Hypatia Sans Pro Light
Look and feel

```html
<!DOCTYPE html>
<html lang="en">
<head>
<meta charset="utf-8">
<title>Harlow Stonefield Civil Construction</title>
<link href="https://fonts.googleapis.com/css2?family=Poppins:wght@300;400;500;600&family=Russo+One&display=swap" rel="stylesheet">
<style>
  :root {
    --brand-blue: #3652a3;
    --ink: #1d1d1f;
    --nav-ink: #3a3a3a;
    --frame-gray: #6f6f6f;
    --label-bg: rgba(238, 238, 238, 0.92);
    --white: #ffffff;
  }
  * { box-sizing: border-box; margin: 0; padding: 0; }
  html, body { width: 976px; height: 1200px; overflow: hidden; background: var(--white); }
  body { font-family: "Poppins", sans-serif; color: var(--ink); }
  .page { position: relative; width: 976px; height: 1200px; }

  .brand { position: absolute; display: flex; align-items: center; gap: 8px; color: var(--brand-blue); font-family: "Poppins", sans-serif; font-weight: 500; text-transform: uppercase; }
  .brand-square { background: var(--brand-blue); }
  .brand-name { line-height: 1.15; letter-spacing: 0.06em; }

  .site-header .brand { left: 115px; top: 16px; }
  .site-header .brand-square { width: 40px; height: 40px; }
  .site-header .brand-name { font-size: 15px; }

  .main-nav { position: absolute; top: 34px; left: 565px; display: flex; gap: 0; font-size: 11.5px; }
  .main-nav a { position: absolute; white-space: nowrap; color: var(--nav-ink); text-decoration: none; }
  .main-nav a.active { color: var(--brand-blue); font-weight: 500; }

  .hero { position: absolute; top: 70px; left: 0; width: 976px; height: 437px; background: linear-gradient(180deg, #656a8c 0%, #5d6180 45%, #3a3c4e 72%, #111116 88%, #07070a 100%); }
  .service-card { position: absolute; top: 40px; width: 175px; height: 225px; }
  .service-photo { position: absolute; inset: 0; }
  .service-label { position: absolute; left: 0; width: 100%; height: 34px; display: flex; align-items: center; justify-content: center; background: var(--label-bg); color: #333; font-size: 12.6px; }
  .service-label.highlight { background: rgba(54, 82, 163, 0.92); color: var(--white); }

  .tagline { position: absolute; top: 530px; left: 0; width: 976px; text-align: center; color: var(--brand-blue); font-size: 33px; font-weight: 400; line-height: 38px; }

  .about-frame { position: absolute; left: 111px; top: 639px; width: 296px; height: 403px; background: var(--frame-gray); }
  .about-photo { position: absolute; left: 117px; top: 615px; width: 303px; height: 418px; background: linear-gradient(180deg, #a9cbe8 0%, #c9d9e4 35%, #b9b3a4 60%, #8e9a80 100%); }

  .about-title { position: absolute; left: 448px; top: 638px; font-family: "Russo One", sans-serif; font-size: 37px; color: var(--brand-blue); text-shadow: 2px 3px 4px rgba(0,0,0,0.2); }
  .about-copy { position: absolute; left: 447px; width: 412px; font-size: 10.3px; line-height: 21.8px; color: var(--ink); }
  .about-copy.first { top: 692px; }
  .about-copy.second { top: 831px; }

  .cta-button { position: absolute; left: 449px; top: 973px; width: 133px; height: 29px; background: var(--brand-blue); color: var(--white); font-size: 12.4px; font-weight: 600; display: flex; align-items: center; justify-content: center; box-shadow: 0 4px 6px rgba(0,0,0,0.3); text-decoration: none; }

  .contact-line { position: absolute; top: 1017px; display: flex; align-items: center; gap: 6px; font-size: 11.5px; font-weight: 500; color: var(--ink); }
  .contact-line.phone { left: 449px; top: 1020px; }
  .contact-line.email { left: 573px; top: 1016px; }
  .contact-line svg { width: 17px; height: 17px; }

  .site-footer .brand { left: 402px; top: 1095px; gap: 6px; }
  .site-footer .brand-square { width: 26px; height: 26px; }
  .site-footer .brand-name { font-size: 10px; }

  .footer-nav { position: absolute; top: 1141px; left: 0; font-size: 11.5px; }
  .footer-nav a { position: absolute; white-space: nowrap; color: var(--nav-ink); text-decoration: none; }

  .copyright { position: absolute; left: 0; top: 1171px; width: 976px; height: 29px; background: var(--brand-blue); color: var(--white); font-size: 10px; display: flex; align-items: center; justify-content: center; }
</style>
</head>
<body>
<div class="page">

  <header class="site-header">
    <div class="brand">
      <span class="brand-square"></span>
      <span class="brand-name">Harlow Stonefield<br>Civil Construction</span>
    </div>
    <nav class="main-nav">
      <a class="active" href="#" style="left:0">Home</a>
      <a href="#" style="left:58px;top:-1px">Project Gallery</a>
      <a href="#" style="left:165px">Careers</a>
      <a href="#" style="left:232px">Contact Us</a>
    </nav>
  </header>

  <section class="hero" role="img" aria-label="Dusk sky with silhouettes of an excavator and heavy trucks on the horizon">
    <div class="service-card" style="left:114px">
      <div class="service-photo" role="img" aria-label="Aerial view of wooded land being cleared for development" style="background:linear-gradient(180deg,#5d7a4c 0%,#8c9a7e 45%,#4f7a3c 80%,#3d6b3a 100%)"></div>
      <div class="service-label" style="top:160px">Land Development</div>
    </div>
    <div class="service-card" style="left:304px">
      <div class="service-photo" role="img" aria-label="Yellow loader digging a trench for underground utilities" style="background:linear-gradient(180deg,#6f8d5b 0%,#d8d6cf 25%,#c9a84a 45%,#6b6157 70%,#d7d3c9 100%)"></div>
      <div class="service-label highlight" style="top:95px">Underground Utilities</div>
    </div>
    <div class="service-card" style="left:496px">
      <div class="service-photo" role="img" aria-label="Yellow excavator against a blue sky" style="background:linear-gradient(180deg,#4a86d6 0%,#8fb6e6 35%,#d8a530 60%,#6c5a4a 100%)"></div>
      <div class="service-label" style="top:160px">Excavation &amp; Grading</div>
    </div>
    <div class="service-card" style="left:685px">
      <div class="service-photo" role="img" aria-label="Aerial view of a highway beside a stabilized drainage channel" style="background:linear-gradient(90deg,#5f7a55 0%,#7f8f78 40%,#9ea3a6 65%,#6f7c6a 100%)"></div>
      <div class="service-label" style="top:162px">Channel Stabilization</div>
    </div>
  </section>

  <h1 class="tagline">We Provide Reliable And Qualitative<br>Construction</h1>

  <section class="about">
    <div class="about-frame"></div>
    <div class="about-photo" role="img" aria-label="Engineer in hard hat and safety vest reviewing plans above a city skyline"></div>
    <h2 class="about-title">About Us</h2>
    <p class="about-copy first">Lorem ipsum dolor sit amet, consectetuer adipiscing elit, sed diam nonummy nibh euismod tincidunt ut laoreet dolore magna aliquam erat volutpat. Ut wisi enim ad minim veniam, quis nostrud exerci tation ullamcorper suscipit lobortis nisl ut aliquip ex ea commodo consequat. Duis autem vel eum iriure dolor in hendrerit in vulputate velit esse molestie consequat, vel illum dolore eu feugiat nulla facilisis at vero eros et accumsan et iusto odio</p>
    <p class="about-copy second">Lorem ipsum dolor sit amet, consectetuer adipiscing elit, sed diam nonummy nibh euismod tincidunt ut laoreet dolore magna aliquam erat volutpat. Ut wisi enim ad minim veniam, quis nostrud exerci tation ullamcorper suscipit lobortis nisl ut aliquip ex ea commodo consequat. Duis autem vel eum iriure dolor in hendrerit in vulputate velit esse molestie consequat, vel illum dolore eu feugiat nulla facilisis at vero eros et accumsan et iusto odio</p>
    <a class="cta-button" href="#">Contact Us Today</a>
    <div class="contact-line phone">
      <svg viewBox="0 0 24 24" fill="none" stroke="#3652a3" stroke-width="1.4" stroke-linecap="round" stroke-linejoin="round"><path d="M5 3.5l3 0.3 1.6 4-2 1.5a11 11 0 0 0 7 7l1.5-2 4 1.6.3 3a2 2 0 0 1-2 2A17 17 0 0 1 3 5.5a2 2 0 0 1 2-2z"/><path d="M14 3a7 7 0 0 1 7 7"/><path d="M14 6.5a3.5 3.5 0 0 1 3.5 3.5"/></svg>
      <span>555.014.2210</span>
    </div>
    <div class="contact-line email">
      <svg viewBox="0 0 24 24" fill="none" stroke="#3652a3" stroke-width="1.4" stroke-linejoin="round"><path d="M3 10l9-6 9 6v10H3z"/><path d="M3 10l9 6 9-6"/><path d="M3 20l7-5M21 20l-7-5"/></svg>
      <span>inquiry@hscivilconstruction.com</span>
    </div>
  </section>

  <footer class="site-footer">
    <div class="brand">
      <span class="brand-square"></span>
      <span class="brand-name">Harlow Stonefield<br>Civil Construction</span>
    </div>
    <nav class="footer-nav">
      <a href="#" style="left:337px">Home</a>
      <a href="#" style="left:389px;top:-1px">Project Gallery</a>
      <a href="#" style="left:495px">Careers</a>
      <a href="#" style="left:564px">Contact Us</a>
    </nav>
    <div class="copyright">Copyright © 2019 Harlow Stonefield Civil Construction. All Rights Reserved.</div>
  </footer>

</div>
</body>
</html>
```